Vireno Subscription Infographic

I need an infographic to promote my new subscription service.
The infographic should be clear and consise, showcasing the benefits and the value of my offering.
I have provided a PDF that describes the service, and the offering in detail. I would like the designer to read the pdf document, understand the offering and design a one page infographic that will condense the information in a nice, visual way, to be shared within Workvine for advertisment purposes.

```html
<!DOCTYPE html>
<html lang="en">
<head>
<meta charset="utf-8">
<title>Vireno Subscription and Benefits</title>
<link href="https://fonts.googleapis.com/css2?family=Roboto+Condensed:wght@700&family=Roboto:wght@300;400;500;700;900&display=swap" rel="stylesheet">
<style>
:root{
  --backdrop:#403e52;
  --navy:#232a5c;
  --ink:#2b2b33;
  --starter:#b8a07c;
  --starter-tint:#f3ede3;
  --entry:#5a5a5f;
  --entry-tint:#f1f1f2;
  --member:#d1951a;
  --member-tint:#fcf3d8;
  --premium:#5a5a5f;
  --premium-tint:#eeeeef;
  --exclusive:#8556c1;
  --exclusive-tint:#ece7f5;
  --bar-track:#e6e7ea;
  --bar-yellow:#ecb93a;
  --bar-green:#8cc63f;
  --bar-blue:#29abe2;
  --bar-orange:#f7941d;
  --white:#ffffff;
}
*{box-sizing:border-box;margin:0;padding:0}
html,body{width:907px;height:1200px;overflow:hidden;background:var(--backdrop)}
body{font-family:"Roboto",sans-serif;color:var(--ink)}
.page{position:relative;width:907px;height:1200px}
.sheet{position:absolute;left:89px;top:83.5px;width:730px;height:1032px;background:var(--navy);overflow:hidden}
.abs{position:absolute}

/* plans background band */
.plans-band{left:0;top:72px;width:730px;height:444px;background:linear-gradient(180deg,#fbfbfc,#f1f1f4)}

/* header */
.masthead{left:0;top:0;width:730px;height:72px;background:var(--navy)}
.brand{left:46px;top:20px;display:flex;align-items:center;gap:6px;color:var(--white);font-weight:700;font-size:24px;letter-spacing:.3px}
.brand-dot{width:30px;height:30px;border-radius:50%;border:3px solid var(--white)}
.masthead-title{left:185px;top:22px;width:500px;text-align:center;color:var(--white);font-family:"Roboto Condensed",sans-serif;font-weight:700;font-size:24px;letter-spacing:2.4px;white-space:nowrap}

.plans-backing{left:49px;top:98px;width:626px;height:268px;background:var(--navy)}
.card{position:absolute;top:80.5px;width:118px;height:296px;border-radius:0 0 7px 7px;overflow:hidden;box-shadow:0 0 0 1px rgba(0,0,0,.08)}
.card.starter{left:49px;background:linear-gradient(180deg,#fff 30%,#e4d6c2);--accent:var(--starter);--tint:var(--starter-tint);--tick:#c9b28e}
.card.entry{left:176px;background:linear-gradient(180deg,#fff 40%,#e6e6e7);--accent:var(--entry);--tint:var(--entry-tint);--tick:#b9b9bd}
.card.member{left:303px;background:linear-gradient(180deg,#fff 35%,#f8dd85);--accent:var(--member);--tint:var(--member-tint);--tick:#e7b230}
.card.premium{left:430px;background:linear-gradient(180deg,#fff 60%,#cfcfd2);--accent:var(--premium);--tint:var(--premium-tint);--tick:#6e6e73}
.card.exclusive{left:557px;background:#fff;border:1px solid #b79be0;--accent:var(--exclusive);--tint:var(--exclusive-tint);--tick:#8556c1}
.tab{position:absolute;left:6px;top:0;width:106px;height:49px;clip-path:polygon(0 0,100% 0,100% 74%,50% 100%,0 74%);display:flex;justify-content:center;padding-top:12px;font-family:"Roboto Condensed",sans-serif;font-weight:700;font-size:16px;letter-spacing:1.6px;color:var(--white)}
.starter .tab{background:linear-gradient(180deg,#c6ad88,#dccdb6)}
.entry .tab{background:linear-gradient(180deg,#d9d9dc,#f6f6f7);color:#111}
.member .tab{background:linear-gradient(180deg,#f7b52a,#f6d35d)}
.premium .tab{background:linear-gradient(180deg,#616165,#c9c9cc)}
.exclusive .tab{background:linear-gradient(180deg,#7f4fbd,#c6b0e6)}
.rows{position:absolute;left:2px;right:2px;top:54px}
.row{height:18px;display:flex;align-items:center;padding-left:8px}
.row:nth-child(odd){background:var(--tint)}
.row .label{width:67px;font-size:5px;color:#333}
.row .value{font-size:9.5px;font-weight:700;color:var(--accent)}
.card.entry .row .value,.card.premium .row .value{color:#555}
.row.blank{height:16px;margin-top:3px;background:var(--tint)}
.features{position:absolute;left:10px;right:4px;top:153px;list-style:none;font-size:6.8px;line-height:8.3px;color:#333}
.features li{position:relative;padding-left:11px;margin-bottom:6.5px}
.features b{font-weight:700;color:#222}
.features li::before{content:"";position:absolute;left:0;top:2px;width:5.5px;height:5.5px;border-radius:50%;background:var(--tick)}
.features li::after{content:"";position:absolute;left:1.9px;top:2.9px;width:1.3px;height:2.4px;border:solid #fff;border-width:0 .8px .8px 0;transform:rotate(45deg)}

/* support list */
.fte-badge{left:26px;top:393px;width:112px;height:112px;border-radius:50%;background:linear-gradient(160deg,#252d63 55%,#6c6aa3);box-shadow:0 0 0 4px #fff,2px 3px 8px rgba(0,0,0,.25);display:flex;align-items:center;justify-content:center;text-align:center;color:var(--white);font-weight:700;font-size:11.5px;line-height:13.5px;padding:0 6px}
.support-list{left:152px;top:397px;width:201px;list-style:none;font-size:7px;font-weight:500;color:#2a2f5a}
.support-list li{border-bottom:.8px solid #3a4173;padding:2.6px 0 3.2px}
.support-list li:first-child{color:#666;line-height:8.4px}
.support-list li:first-child b{color:#2a2f5a}
.divider-dotted{left:377px;top:391px;height:114px;border-left:1px dashed #9a9aa8}
.terms{left:394px;top:396px;width:292px;font-size:10px;line-height:11.5px;color:#333}
.terms p{padding-bottom:5px;margin-bottom:5.5px;border-bottom:.8px solid #9a9aa8}
.terms p:last-child{border-bottom:0}
.terms b{font-weight:700;color:#111}

/* team */
.team-title{left:0;top:544px;width:730px;text-align:center;color:var(--white);font-family:"Roboto Condensed",sans-serif;font-weight:700;font-size:23px;letter-spacing:2.4px;white-space:nowrap}
.lead-pill{left:241px;top:588.5px;width:254px;height:30px;border-radius:15px;background:var(--white);box-shadow:0 3px 0 #5a5f93;display:flex;align-items:center;justify-content:center;color:var(--navy);font-weight:700;font-size:11.5px}
.lead-note{left:150px;top:632px;width:436px;text-align:center;color:#e8e9f4;font-weight:300;font-size:10.5px;line-height:12.5px}
.connectors{left:0;top:0;width:730px;height:1032px;pointer-events:none}
.role{position:absolute;top:700px;width:100px;text-align:center;color:var(--white);font-weight:700;font-size:6.8px;line-height:8.2px}
.role small{display:block;font-weight:400;font-size:6.6px;color:#d9dbeb}
.role-card{position:absolute;top:722.5px;width:89px;height:94px;background:var(--white);border-radius:0 0 45px 45px/0 0 44px 44px;box-shadow:0 5px 0 #454a85;padding:10px 4px 0 8px}
.role-card ul{list-style:none;font-size:6.7px;line-height:7.8px;color:#2d3670}
.role-card li{position:relative;padding-left:9px;padding-bottom:2.6px;margin-bottom:2.6px;border-bottom:.6px solid #e1e2ea}
.role-card li:last-child{border-bottom:0}
.role-card li::before{content:"";position:absolute;left:0;top:1px;width:5.5px;height:5.5px;border-radius:50%;background:var(--navy)}
.role-card li::after{content:"";position:absolute;left:1.9px;top:1.9px;width:1.3px;height:2.4px;border:solid #fff;border-width:0 .8px .8px 0;transform:rotate(45deg)}

/* utilisation chart */
.chart{left:26px;top:842px;width:350px;height:190px;border-radius:8px 8px 0 0;background:linear-gradient(180deg,#2f3a78,var(--navy) 60%)}
.chart-title{position:absolute;left:0;top:9px;width:350px;text-align:center;color:var(--white);font-weight:700;font-size:14px;line-height:17px}
.bar{position:absolute;left:8px;width:306px;height:12px;border-radius:6px;background:var(--bar-track);overflow:hidden}
.bar .fill{position:absolute;left:0;top:0;bottom:0;border-radius:6px;color:var(--white);font-weight:700;font-size:7.5px;line-height:12px;text-align:right;padding-right:15px}
.bar .name{position:absolute;right:15px;top:0;font-size:7px;line-height:12px;color:#80828c;letter-spacing:.6px}
.agile{left:407px;top:875px;width:300px;color:#eef0f8;font-weight:300;font-size:12.4px;line-height:14.6px}
.agile b{font-weight:700;color:var(--white)}
.site{left:407px;top:980px;color:var(--white);font-size:14px;letter-spacing:3.2px}
</style>
</head>
<body>
<div class="page">
<main class="sheet">

  <div class="abs plans-band"></div>

  <header class="abs masthead">
    <div class="abs brand"><span class="brand-dot"></span>Vireno</div>
    <h1 class="abs masthead-title">VIRENO SUBSCRIPTION AND BENEFITS</h1>
  </header>

  <div class="abs plans-backing"></div>

  <article class="card starter">
    <div class="tab">STARTER</div>
    <div class="rows">
      <div class="row"><span class="label">Full Time Equivalent (FTE)</span><span class="value">1 FTE</span></div>
      <div class="row"><span class="label">Price (Monthly)</span><span class="value">£9,280</span></div>
      <div class="row"><span class="label">Engineering Hours Pool</span><span class="value">160</span></div>
      <div class="row"><span class="label">Equivalent Hourly Price</span><span class="value">£58</span></div>
      <div class="row blank"></div>
    </div>
    <ul class="features">
      <li>Online Support only</li>
      <li><b>Mainstream Tools</b><br>Emails accounts Deskwise<br>Office Plangantt</li>
    </ul>
  </article>

  <article class="card entry">
    <div class="tab">ENTRY</div>
    <div class="rows">
      <div class="row"><span class="label">Full Time Equivalent (FTE)</span><span class="value">2 FTE</span></div>
      <div class="row"><span class="label">Price (Monthly)</span><span class="value">£17,120</span></div>
      <div class="row"><span class="label">Engineering Hours Pool</span><span class="value">320</span></div>
      <div class="row"><span class="label">Equivalent Hourly Price</span><span class="value">£53.5</span></div>
      <div class="row blank"></div>
    </div>
    <ul class="features">
      <li>1 Engineer Semi-pernam<br>enently on Site</li>
      <li><b>Mainstream Tools</b><br>Emails accounts Deskwise<br>Office Plangantt</li>
      <li>Reliqa Vireno In house<br>Calculators</li>
    </ul>
  </article>

  <article class="card member">
    <div class="tab">MEMBER</div>
    <div class="rows">
      <div class="row"><span class="label">Full Time Equivalent (FTE)</span><span class="value">3 FTE</span></div>
      <div class="row"><span class="label">Price (Monthly)</span><span class="value">£24,900</span></div>
      <div class="row"><span class="label">Engineering Hours Pool</span><span class="value">480</span></div>
      <div class="row"><span class="label">Equivalent Hourly Price</span><span class="value">£51.9</span></div>
      <div class="row blank"></div>
    </div>
    <ul class="features">
      <li>Online Support only</li>
      <li><b>Mainstream Tools</b><br>Emails accounts Deskwise<br>Office Plangantt</li>
      <li>Reliqa Vireno In house<br>Calculators</li>
      <li><b>Specialist Tools</b><br>NumoraFlowsim</li>
    </ul>
  </article>

  <article class="card premium">
    <div class="tab">PREMIUM</div>
    <div class="rows">
      <div class="row"><span class="label">Full Time Equivalent (FTE)</span><span class="value">4 FTE</span></div>
      <div class="row"><span class="label">Price (Monthly)</span><span class="value">£32,000</span></div>
      <div class="row"><span class="label">Engineering Hours Pool</span><span class="value">640</span></div>
      <div class="row"><span class="label">Equivalent Hourly Price</span><span class="value">£50</span></div>
      <div class="row blank"></div>
    </div>
    <ul class="features">
      <li>Online Support only</li>
      <li><b>Mainstream Tools</b><br>Emails accounts Deskwise<br>Office Plangantt</li>
      <li>Reliqa Vireno In house<br>Calculators</li>
      <li><b>Specialist Tools</b><br>NumoraFlowsim</li>
      <li>High end software<br>RotorDraft Quantix (Mech)</li>
    </ul>
  </article>

  <article class="card exclusive">
    <div class="tab">EXCLUSIVE</div>
    <div class="rows">
      <div class="row"><span class="label">Full Time Equivalent (FTE)</span><span class="value">5 FTE</span></div>
      <div class="row"><span class="label">Price (Monthly)</span><span class="value">£39,600</span></div>
      <div class="row"><span class="label">Engineering Hours Pool</span><span class="value">600</span></div>
      <div class="row"><span class="label">Equivalent Hourly Price</span><span class="value">£49.5</span></div>
      <div class="row blank"></div>
    </div>
    <ul class="features">
      <li>Online Support only</li>
      <li><b>Mainstream Tools</b><br>Emails accounts Deskwise<br>Office Plangantt</li>
      <li>Reliqa Vireno In house<br>Calculators</li>
      <li><b>Specialist Tools</b><br>NumoraFlowsim</li>
      <li>High end software<br>RotorDraft Quantix (Mech)</li>
      <li>Specialist Software Gearon<br>MultiBody Dynamics</li>
    </ul>
  </article>

  <div class="abs fte-badge">See Subscription Levels for FTE Equivalent</div>
  <svg class="abs" style="left:130px;top:396px" width="30" height="110" aria-hidden="true">
    <path d="M4 30 L26 2 M4 80 L26 108" stroke="#3a4173" stroke-width=".8" fill="none"/>
  </svg>
  <ul class="abs support-list">
    <li>Flexible Systems Engineering support including but not limited to: <b>MBSE, FMEA, requirements management and DVP creation</b></li>
    <li>Safety Engineer and DMFEA/Fault Tree Expert Support</li>
    <li>Project Manager and Engineering Management</li>
    <li>Power Electronics and Inverter Development Engineer Support</li>
    <li>Onsite Support (Ashcombe)</li>
    <li>eMachine Design Engineer</li>
  </ul>
  <div class="abs divider-dotted"></div>
  <div class="abs terms">
    <p>Subscription Level can be <b>adjusted on a 3 month notice</b> (higher/lower number of FTE hours)</p>
    <p>If project needs increase, <b>upgrades on the service can be delivered potentially earlier</b>, pending Vireno engineering team availability.</p>
    <p>If project needs are reduced, <b>with a 3 month notice we can reallocate the resources to other customers,</b> effectively being able to reduce the subscription service levels</p>
  </div>

  <h2 class="abs team-title">VIRENO AEROSPACE SYSTEMS ENGINEERING TEAM</h2>

  <svg class="abs connectors" viewBox="0 0 730 1032" aria-hidden="true">
    <g stroke="#ffffff" stroke-width="1" fill="none">
      <line x1="368" y1="619" x2="368" y2="629"/>
      <path d="M359 664 Q368 668 368 656 Q368 668 377 664"/>
      <line x1="368" y1="664" x2="368" y2="694"/>
      <path d="M70 695 Q70 676 85 676 L651 676 Q666 676 666 695"/>
      <path d="M168.5 695 Q168.5 676 183.5 676"/>
      <path d="M267 695 Q267 676 282 676"/>
      <path d="M469 695 Q469 676 454 676"/>
      <path d="M567 695 Q567 676 552 676"/>
    </g>
    <g fill="#232a5c" stroke="#ffffff" stroke-width="1">
      <circle cx="70" cy="695" r="3"/><circle cx="168.5" cy="695" r="3"/><circle cx="267" cy="695" r="3"/>
      <circle cx="368" cy="695" r="3"/><circle cx="469" cy="695" r="3"/><circle cx="567" cy="695" r="3"/><circle cx="666" cy="695" r="3"/>
    </g>
  </svg>

  <div class="abs lead-pill">Team Leader &amp; Principal Project Manager</div>
  <p class="abs lead-note">Team Leadership - Task allocation and deliverables agreement<br>based on the level of the subscription service</p>

  <div class="role" style="left:20px">Electric Motor Design Expert</div>
  <div class="role" style="left:118.5px">Requirements Engineer<small>(Based in Ashcombe)</small></div>
  <div class="role" style="left:217px">Requirements Engineer</div>
  <div class="role" style="left:318px;top:696px">Systems Safety and<br>DFMEA Expert</div>
  <div class="role" style="left:419px;top:696px">Power Electronics and<br>Controls Engineer</div>
  <div class="role" style="left:517px;top:696px">Test and Validation<br>Engineer</div>
  <div class="role" style="left:616px">Mechanical Engineer</div>

  <div class="role-card" style="left:25px"><ul>
    <li>Thermal analysis</li><li>Electrical analysis</li><li>Mechanical analysis</li><li>CFD and Specialised</li><li>Analysis Support</li></ul></div>
  <div class="role-card" style="left:124px"><ul>
    <li>Requirements Management</li><li>System Breakdown Analysis</li><li>Boundary Diagrams</li><li>Engineering Support</li></ul></div>
  <div class="role-card" style="left:223px"><ul>
    <li>Requirements Management</li><li>System Breakdown Analysis</li><li>Boundary Diagrams</li><li>Engineering Support</li></ul></div>
  <div class="role-card" style="left:321px;padding-top:9px"><ul>
    <li>DFMEA</li><li>FTA</li><li>Flight Safety Assessement</li><li>Support Safety Principles Engineering</li></ul></div>
  <div class="role-card" style="left:419px;padding-top:9px"><ul>
    <li>Inverter HW Expertise</li><li>Software Support</li><li>Controls Engineering Development</li><li>Leadership for Tier1</li></ul></div>
  <div class="role-card" style="left:517.5px;padding-top:8px"><ul>
    <li>DVP Development</li><li>DVP Execution Support</li><li>Test Results Evaluation</li><li>Test Robustness Validation</li></ul></div>
  <div class="role-card" style="left:616px"><ul>
    <li>Mechanical Calculations</li><li>Mechanical Designs and Drawings</li><li>CAD Support</li><li>Structural Analysis</li></ul></div>

  <section class="abs chart">
    <h3 class="chart-title">Utilization Needed Per Type of Engineer -<br>Sorted by Importance</h3>
    <div class="bar" style="top:51px"><span class="name">Systems Engineering</span><div class="fill" style="width:52%;background:var(--bar-yellow)">25%</div></div>
    <div class="bar" style="top:70px"><span class="name">Test &amp; Validation Engineering</span><div class="fill" style="width:46.5%;background:var(--bar-green)">20%</div></div>
    <div class="bar" style="top:88.5px"><span class="name">Electronics and Control</span><div class="fill" style="width:46.5%;background:var(--bar-green)">20%</div></div>
    <div class="bar" style="top:107px"><span class="name">Mechanical Engineering</span><div class="fill" style="width:37%;background:var(--bar-blue)">15%</div></div>
    <div class="bar" style="top:126px"><span class="name">System Safety</span><div class="fill" style="width:27%;background:var(--bar-orange)">10%</div></div>
    <div class="bar" style="top:144px"><span class="name">Electric Motor Design</span><div class="fill" style="width:27%;background:var(--bar-orange)">10%</div></div>
  </section>

  <p class="abs agile">In our proposed Engineering Subscription Service, the heart of its operation will be rooted in the <b>Agile project management methodology</b>. Every Monday, a focused alignment Sprint Design meeting will be set between our Project Manager and the Lead Customer Engineer from Skyvolt .</p>
  <p class="abs site">www.vireno-technology.co.uk</p>

</main>
</div>
</body>
</html>
```